Brazilian wine business need a label for a sparkling wine

We are importing a new italian sparkling wine, but we need to build our own brand. Our main focus is to sell sparkling wine for events, specially for weddings. So, specially for this audience, presentation is key.
We like to see wine in a "uncomplicated" way.
It is a mid price product.
The foil capsule color must be black, white or silver, due to production restrictions. We cannot have any graphic interference in this part, also.

We need to develop a label for it. The name will be "Lumera Brut" (means "hug" in italian).

Our main public is people around the early 30s, so it should look modern and clean.
It is good, but not mandatory, to have a few information at the front label:
- Alcohol % (12%)
- Origin (Italy)

We need to avoid a few colours, for different reasons:
- Don´t use yellow/orange: too linked to Maison Dravelle;
- Don´t use red or pink: people think it is a rosé, but it is a white.
Our idea is to work with white and blue or turquoise, maybe a green, something like that. Can have a touch of gold, also. (more references in the color tab below)
- The bottle is black.

Industry/Entity Type

Business

Font styles to use
Other font styles liked:
• Berlin Sans FB Regular or something less "round" but similar to Cooper Black Regular

Colors
00a990
33b8a4

Requirements
Must have
• As the name means "hug", we want to have a graphic symbol that represents connections, alliances, symbiosis or infinite. I attached a few symbols that could be explore, but of course you can bring differente suggestions.
• We need a clean design, nothing with too many information.

```html
<!DOCTYPE html>
<html lang="en">
<head>
<meta charset="utf-8">
<title>Lumera Brut – Front Label</title>
<link rel="stylesheet" href="https://fonts.googleapis.com/css2?family=Cinzel:wght@400;600;700&family=Cormorant+Garamond:ital,wght@0,500;0,600;1,500&display=swap">
<style>
  :root {
    --backdrop: #2a2b2d;
    --paper: #fbfdfd;
    --paper-pattern: #eef4f5;
    --teal: #a9ddd6;
    --teal-deep: #7fc8bd;
    --teal-ink: #5fb3a6;
    --silver-light: #f4f5f6;
    --silver: #c9cdd0;
    --silver-dark: #8d9396;
    --ink-grey: #6f7578;
    --ink-soft: #9aa2a5;
    --white: #ffffff;
  }
  * { box-sizing: border-box; margin: 0; padding: 0; }
  html, body { width: 1200px; height: 1000px; overflow: hidden; }
  body { background: var(--backdrop); position: relative; font-family: "Cormorant Garamond", Georgia, serif; }

  .label {
    position: absolute; left: 100px; top: 110px; width: 1000px; height: 780px;
    background: var(--paper);
    border: 3px solid var(--silver);
    border-radius: 10px;
    box-shadow: inset 0 0 0 9px var(--paper), inset 0 0 0 11px var(--silver-dark);
  }
  .label-pattern {
    position: absolute; inset: 22px; border-radius: 4px;
    background: var(--paper-pattern);
  }
  .label-art { position: absolute; inset: 0; width: 1000px; height: 780px; }

  .origin-tag {
    position: absolute; left: 500px; top: 90px; transform: translateX(-50%);
    font-family: "Cinzel", "Times New Roman", serif; font-weight: 600;
    font-size: 22px; letter-spacing: 4px; color: var(--white);
    white-space: nowrap;
  }
  .fine-print {
    position: absolute; left: 0; width: 100%; text-align: center;
    font-size: 19px; color: var(--ink-soft); letter-spacing: 0.5px;
  }
  .fine-print--top { top: 150px; }
  .fine-print--middle { top: 500px; }
  .fine-print--bottom { top: 628px; }

  .brand-name {
    position: absolute; left: 0; width: 100%; top: 218px; text-align: center;
    font-family: "Cinzel", "Times New Roman", serif; font-weight: 700;
    font-size: 118px; letter-spacing: 14px; color: var(--white);
    line-height: 1;
  }
  .vintage {
    position: absolute; left: 500px; top: 352px; transform: translateX(-50%);
    font-family: "Cinzel", "Times New Roman", serif; font-weight: 600;
    font-size: 30px; letter-spacing: 6px; color: var(--ink-grey);
  }
  .style-name {
    position: absolute; left: 0; width: 100%; top: 410px; text-align: center;
    font-family: "Cinzel", "Times New Roman", serif; font-weight: 400;
    font-size: 76px; letter-spacing: 22px; color: var(--ink-grey);
    line-height: 1;
  }
  .volume {
    position: absolute; left: 52px; top: 700px;
    font-style: italic; font-size: 28px; color: var(--ink-grey);
  }
</style>
</head>
<body>
  <main class="label">
    <div class="label-pattern" role="img" aria-label="Fine silver guilloche line pattern across the label"></div>

    <svg class="label-art" viewBox="0 0 1000 780" aria-hidden="true">
      <!-- origin tag -->
      <rect x="340" y="82" width="320" height="44" rx="6" fill="var(--teal-deep)" stroke="var(--silver)" stroke-width="3"/>

      <!-- main name band -->
      <path d="M80 190 Q500 160 920 190 L900 250 L920 340 Q500 310 80 340 L100 250 Z"
            fill="var(--silver-light)" stroke="var(--silver-dark)" stroke-width="3"/>
      <path d="M100 202 Q500 174 900 202 L884 250 L900 328 Q500 298 100 328 L116 250 Z"
            fill="var(--teal)" stroke="var(--silver)" stroke-width="4"/>

      <!-- vintage badge -->
      <rect x="390" y="342" width="220" height="54" rx="27" fill="var(--silver-light)" stroke="var(--silver-dark)" stroke-width="3"/>
      <rect x="400" y="350" width="200" height="38" rx="19" fill="none" stroke="var(--silver)" stroke-width="2"/>

      <!-- rules beside style name -->
      <line x1="150" y1="455" x2="270" y2="455" stroke="var(--silver-dark)" stroke-width="2"/>
      <line x1="730" y1="455" x2="850" y2="455" stroke="var(--silver-dark)" stroke-width="2"/>
    </svg>

    <svg class="label-art" viewBox="0 0 1000 780">
      <rect x="350" y="550" width="300" height="56" rx="28" fill="var(--silver)" opacity="0.55"
            role="img" aria-label="Silver scrollwork ornament"/>
    </svg>

    <p class="origin-tag">PRODUCE OF ITALY</p>
    <p class="fine-print fine-print--top">Sparkling wine from the hills of northern Italy</p>
    <h1 class="brand-name">LUMERA</h1>
    <p class="vintage">MMXVII</p>
    <p class="style-name">BRUT</p>
    <p class="fine-print fine-print--middle">Crisp, bright and made for every celebration</p>
    <p class="fine-print fine-print--bottom">Serve chilled and share with the people you love</p>
    <p class="volume">750 ml</p>
  </main>
</body>
</html>
```